Need App for Impact Related Events

My app is to help with internal events. When you enter the prompted event code the next screen shows you everyone currently at the event. It will give you the ability to Start a conversation with someone you met at that event, or signal it is your turn to send a message. The next screen is a message thread with that person. I am looking for a design that incorporates the colors and ‘feel good’ emotion of our logo. I have pieced together a pretty good interpretation of what I’m looking for in the attached mockup by slicing and dicing designs. I also attached our logo mascot.Screens (see attached mockups)

Note 1: I do not like the picture on the screen used in screen one because it makes it seem like a dating app. I attached an alternative photo that can be used or present different ideas.

Note 2: On the login/signup screen (screen 2) I need an additional first and last name for login, you can try to fit this on one login screen or present a two step signup screen where that is presented in the second screen.

READ MOCKUP GUIDELINES UNDER Must Haves

Target Market(s)

People attending internal social impact events

Industry/Entity Type

Charity

Font styles to use
Sans Serif

Colors
86cfc6

Requirements
Must have
• Follow the screen mockups attached to project
• PLEASE READ
• I have provided a relatively close design of what I’m looking for in the mockups. Some screens need to be followed more closely to my design mockup than other. I have listed a guide below how how closely you should follow my mockup design exactly. Overall I would like to see some ideas of incorporating a few accent colors so it doesn’t appear SO Blue. I also attached some app inspiration designs I found from around the web
• Screen Mockup Guideline Follow %
• Screen 1: 65% - mostly on target, would like to see ways to make it not SO Blue and possibly creative places to add some explainer text describing the app
• Screen 2: 50% - general design idea is here, but more open
• Screen 3: 35% - a lot more room for design influence
• Screen 4: 70% - mostly on target, a little room for design influence/color scheme ideas
• Screen 5-6: 25% - a lot of room for design change/ideas/influence
• Screen 7-8: 80% - already very close to what I need, maybe open to slight sizing and color scheme ideas
• Screen 9: 15% - the most open for influence, only the general functionality of the screen is communicated here
Nice to have
• Please Read Mockup Guideline above. In large part I am looking for something to use some nice accent colors so it is not overwhelmingly blue and bring the whole design into a seamless style.
Should not have

```html
<!DOCTYPE html>
<html lang="en">
<head>
<meta charset="utf-8">
<title>Who you've met</title>
<link rel="stylesheet" href="https://fonts.googleapis.com/css2?family=Nunito+Sans:wght@400;600;700&display=swap">
<style>
  :root {
    --header-start: #2db7d5;
    --header-end: #5fe6e9;
    --page-bg: #eef2f5;
    --card-bg: #ffffff;
    --ink: #1f2326;
    --muted: #9aa1a6;
    --count: #7d858a;
    --start-green: #5dd6a3;
    --turn-blue: #36c0dc;
    --tab-active: #38b4d6;
    --tab-idle: #7c8388;
    --divider: #dfe4e7;
    --avatar-tone: #a0705a;
    --avatar-tone-2: #5b3a2e;
    --white: #ffffff;
  }
  * { box-sizing: border-box; margin: 0; padding: 0; }
  html, body { width: 675px; height: 1200px; overflow: hidden; }
  body {
    position: relative;
    background: var(--page-bg);
    font-family: "Nunito Sans", sans-serif;
    color: var(--ink);
  }
  .app-header {
    position: absolute; left: 0; top: 0; width: 675px; height: 162px;
    background: linear-gradient(90deg, var(--header-start), var(--header-end));
    color: var(--white);
  }
  .status-bar {
    position: absolute; left: 0; top: 0; width: 675px; height: 36px;
    font-size: 21px; font-weight: 600;
  }
  .status-left { position: absolute; left: 10px; top: 6px; display: flex; align-items: center; gap: 6px; }
  .status-time { position: absolute; left: 0; width: 675px; top: 5px; text-align: center; }
  .status-right { position: absolute; right: 12px; top: 6px; display: flex; align-items: center; gap: 6px; }
  .screen-title {
    position: absolute; left: 0; top: 52px; width: 675px; text-align: center;
    font-size: 29px; font-weight: 700;
  }
  .tabs { position: absolute; left: 0; top: 118px; width: 675px; height: 44px; display: flex; }
  .tab {
    flex: 1; text-align: center; font-size: 22px; font-weight: 700; letter-spacing: 1px;
    opacity: .85;
  }
  .tab.is-active { opacity: 1; }
  .tab-indicator { position: absolute; left: 0; bottom: 0; width: 342px; height: 4px; background: var(--white); }
  .people-count {
    position: absolute; left: 0; top: 196px; width: 675px; text-align: center;
    font-size: 22px; color: var(--count);
  }
  .person-card {
    position: absolute; left: 79px; width: 596px; height: 172px;
    background: var(--card-bg); border-radius: 12px 0 0 12px;
    box-shadow: 0 2px 6px rgba(0,0,0,.04);
  }
  .avatar {
    position: absolute; left: -64px; top: 22px; width: 128px; height: 128px;
    border-radius: 50%; border: 6px solid var(--white);
    background: radial-gradient(circle at 50% 45%, var(--avatar-tone) 0 38%, var(--avatar-tone-2) 70%);
    box-shadow: 0 2px 6px rgba(0,0,0,.12);
  }
  .person-name { position: absolute; left: 85px; top: 52px; font-size: 32px; font-weight: 400; }
  .person-meta { position: absolute; left: 85px; top: 93px; font-size: 22px; color: var(--muted); }
  .action-button {
    position: absolute; left: 407px; top: 22px; width: 164px; height: 126px; border-radius: 5px;
    color: var(--white); font-size: 21px; font-weight: 700; text-align: center;
  }
  .action-button svg { position: absolute; left: 62px; top: 22px; }
  .action-button span { position: absolute; left: 0; width: 164px; top: 78px; }
  .action-start { background: var(--start-green); }
  .action-turn { background: var(--turn-blue); }
  .tab-bar {
    position: absolute; left: 0; top: 1121px; width: 675px; height: 79px;
    background: var(--white); border-top: 1px solid var(--divider); display: flex;
  }
  .tab-item { flex: 1; text-align: center; font-size: 20px; color: var(--tab-idle); padding-top: 8px; }
  .tab-item svg { display: block; margin: 0 auto 2px; }
  .tab-item.is-active { color: var(--tab-active); }
</style>
</head>
<body>
  <header class="app-header">
    <div class="status-bar">
      <div class="status-left">
        <svg width="30" height="16" viewBox="0 0 30 16" fill="#fff"><rect x="0" y="11" width="4" height="5"/><rect x="6" y="8" width="4" height="8"/><rect x="12" y="5" width="4" height="11"/><rect x="18" y="2" width="4" height="14"/></svg>
        <span>Nimbus</span>
        <svg width="24" height="18" viewBox="0 0 24 18" fill="none" stroke="#fff" stroke-width="2.4" stroke-linecap="round"><path d="M2 6a15 15 0 0 1 20 0"/><path d="M6 10a9 9 0 0 1 12 0"/><circle cx="12" cy="14.5" r="1.8" fill="#fff" stroke="none"/></svg>
      </div>
      <div class="status-time">9:41 AM</div>
      <div class="status-right">
        <svg width="12" height="20" viewBox="0 0 12 20" fill="none" stroke="#fff" stroke-width="1.8"><path d="M1 5l10 10-5 4V1l5 4L1 15"/></svg>
        <span>100%</span>
        <svg width="44" height="20" viewBox="0 0 44 20"><rect x="1" y="1" width="38" height="18" rx="4" fill="none" stroke="#fff" stroke-width="2"/><rect x="4" y="4" width="32" height="12" rx="2" fill="#fff"/><rect x="40" y="7" width="3" height="6" rx="1" fill="#fff"/></svg>
      </div>
    </div>
    <h1 class="screen-title">Who you’ve met</h1>
    <nav class="tabs">
      <div class="tab is-active">FOR YOU</div>
      <div class="tab">POPULAR</div>
      <div class="tab-indicator"></div>
    </nav>
  </header>

  <p class="people-count">31 People to meet</p>

  <section class="person-card" style="top:261px">
    <div class="avatar" role="img" aria-label="Attendee profile photo"></div>
    <div class="person-name">Maren T.</div>
    <div class="person-meta">Has met 6 people</div>
    <div class="action-button action-start">
      <svg width="40" height="44" viewBox="0 0 40 44" fill="none" stroke="#fff" stroke-width="2.4" stroke-linejoin="round"><path d="M6 42V3h26l-7 10 7 10H6"/></svg>
      <span>Start</span>
    </div>
  </section>

  <section class="person-card" style="top:457px">
    <div class="avatar" role="img" aria-label="Attendee profile photo"></div>
    <div class="person-name">Maren T.</div>
    <div class="person-meta">Has met 6 people</div>
    <div class="action-button action-turn">
      <svg width="40" height="44" viewBox="0 0 40 44" fill="none" stroke="#fff" stroke-width="2.4" stroke-linecap="round" stroke-linejoin="round"><path d="M6 42V14h30"/><path d="M26 4l10 10-10 10"/></svg>
      <span>Your turn</span>
    </div>
  </section>

  <section class="person-card" style="top:653px">
    <div class="avatar" role="img" aria-label="Attendee profile photo"></div>
    <div class="person-name">Maren T.</div>
    <div class="person-meta">Has met 6 people</div>
    <div class="action-button action-start">
      <svg width="40" height="44" viewBox="0 0 40 44" fill="none" stroke="#fff" stroke-width="2.4" stroke-linejoin="round"><path d="M6 42V3h26l-7 10 7 10H6"/></svg>
      <span>Start</span>
    </div>
  </section>

  <section class="person-card" style="top:849px">
    <div class="avatar" role="img" aria-label="Attendee profile photo"></div>
    <div class="person-name">Maren T.</div>
    <div class="person-meta">Has met 6 people</div>
  </section>

  <section class="person-card" style="top:1045px">
    <div class="avatar" role="img" aria-label="Attendee profile photo"></div>
    <div class="person-name">Maren T.</div>
    <div class="person-meta">Has met 6 people</div>
  </section>

  <nav class="tab-bar">
    <div class="tab-item is-active">
      <svg width="40" height="30" viewBox="0 0 40 30" fill="none" stroke="currentColor" stroke-width="2.4"><circle cx="14" cy="9" r="6"/><path d="M2 28c0-7 5-11 12-11s12 4 12 11z"/><circle cx="27" cy="9" r="6"/><path d="M25 17c7 0 13 4 13 11H26"/></svg>
      People
    </div>
    <div class="tab-item">
      <svg width="40" height="30" viewBox="0 0 40 30" fill="currentColor"><path d="M4 4h20a3 3 0 0 1 3 3v9a3 3 0 0 1-3 3H12l-6 5v-5H4a3 3 0 0 1-3-3V7a3 3 0 0 1 3-3z"/><path d="M30 10h5a3 3 0 0 1 3 3v8a3 3 0 0 1-3 3h-1v4l-5-4h-9a3 3 0 0 1-3-3h11a3 3 0 0 0 2-3z"/></svg>
      Chats
    </div>
    <div class="tab-item">
      <svg width="40" height="30" viewBox="0 0 40 30" fill="none" stroke="currentColor" stroke-width="2.2"><circle cx="20" cy="15" r="4.5"/><path d="M20 2l3 3.5 4.5-1 1 4.5 4.5 1.5-2 4 2 4-4.5 1.5-1 4.5-4.5-1L20 28l-3-3.5-4.5 1-1-4.5L7 19.5l2-4-2-4L11.5 10l1-4.5 4.5 1z" stroke-linejoin="round"/></svg>
      Settings
    </div>
  </nav>
</body>
</html>
```